User Interface Designer Needed

I need a few designs for a property law comparison website. We assist the public with finding a solicitor for the purchase or sale of their house and units. We are currently in the process of creating a questionnaire based woo commerce product filter using gravity forms. I'd like to see designs that use the logo colours. Users will be selecting options such as "Buying" or "Selling", they will then be selecting options such as "House" "Unit" or "Land". Details attached. The final design should communicate ease and simplicity. Questions will be answered one at a time, and the next question is dependent on the answer to the question prior

Target Market(s)

First home buyers, people from ages 18-80 make and female looking to get rid of the hassle of ringing around and going from website to website trying to get a quote

Industry/Entity Type

Real Estate

Number of Pages Required

1 page

Colors
33a6d7

Requirements
Must have
• A design for every question
Nice to have
• Simple symbols or simplistic pictures incorporated, even better if you can turn the question into a picture instead of words eg. A picture of a house, a picture of a unit and a picture of land instead of written answers

```html
<!DOCTYPE html>
<html lang="en">
<head>
<meta charset="utf-8">
<title>Keyvale – Quote Extras</title>
<link href="https://fonts.googleapis.com/css2?family=Open+Sans:ital,wght@0,300;0,400;0,600;0,700;1,400&display=swap" rel="stylesheet">
<style>
:root{
  --brand:#03a4d8;
  --ink:#444;
  --muted:#b9b9b9;
  --line:#d8d8d8;
  --tip:#333333;
  --soft:#e6e6e6;
  --white:#fff;
}
*{box-sizing:border-box;margin:0;padding:0}
html,body{width:1200px;height:1200px;overflow:hidden;background:var(--white)}
body{position:relative;font-family:"Open Sans",Arial,sans-serif;color:var(--ink)}
.abs{position:absolute}

.brand-name{left:144px;top:48px;font-size:32px;font-weight:600;color:var(--brand);letter-spacing:-.5px;line-height:40px;white-space:nowrap}
.brand-dot{display:inline-block;width:12px;height:12px;border-radius:50%;background:var(--brand);margin-right:9px;vertical-align:middle}
.main-nav a{position:absolute;top:59px;font-size:11.5px;color:var(--ink);text-decoration:none;letter-spacing:.2px;white-space:nowrap}
.cart{left:1044px;top:61px}

.steps{left:364px;top:186px;width:466px;height:25px;border-bottom:1px solid var(--line)}
.steps span{position:absolute;top:0;font-size:14.5px;color:var(--muted);font-weight:400;white-space:nowrap}
.steps .current{color:var(--ink)}

.section-title{font-size:38px;font-weight:400;color:var(--ink);line-height:44px;letter-spacing:.3px;white-space:nowrap}
.title-rule{height:2px;background:var(--ink)}

.option{position:absolute;height:64px;border:2px solid var(--brand);background:var(--white);
  display:flex;align-items:center;padding-left:15px;font-size:17.5px;font-weight:700;color:var(--ink);letter-spacing:.3px;white-space:nowrap;overflow:hidden}
.option.selected{background:var(--brand);color:var(--white)}
.info{position:absolute;top:50%;margin-top:-10px;width:20px;height:20px;background:var(--brand);color:var(--white);
  font-style:italic;font-weight:600;font-family:Georgia,serif;font-size:15px;line-height:20px;text-align:center}
.selected .info{background:transparent;border:1.5px solid var(--white);line-height:17px}

.tooltip{left:542px;top:530px;width:288px;height:239px;background:var(--tip);color:var(--white);
  padding:15px 18px 0 20px;font-size:11.3px;line-height:20.8px;z-index:2}
.tooltip::after{content:"";position:absolute;left:130px;bottom:-14px;border:10px solid transparent;border-top:14px solid var(--tip);border-bottom:0}
.tooltip ul{list-style:none}
.tooltip li::before{content:"•";margin-right:6px;font-size:9px}

.radio{position:absolute;left:241px;width:38px;height:38px;border:2.5px solid var(--brand);border-radius:50%}
.radio.checked::after{content:"";position:absolute;left:7px;top:7px;width:19px;height:19px;border-radius:50%;background:var(--brand)}
.radio-label{left:302px;font-size:24px;line-height:36px;font-weight:300;color:var(--ink);white-space:nowrap}

.btn{position:absolute;top:1045px;width:199px;height:52px;display:flex;align-items:center;justify-content:center;font-size:24px;font-weight:400}
.btn-back{left:242px;background:var(--soft);color:var(--ink)}
.btn-submit{left:450px;background:var(--brand);color:var(--white)}
</style>
</head>
<body>

<header>
  <div class="abs brand-name"><span class="brand-dot"></span>Keyvale</div>
  <nav class="main-nav">
    <a style="left:609px">HOME</a>
    <a style="left:663px">FIXED FEES</a>
    <a style="left:740px">ARTICLES</a>
    <a style="left:807px">COMPANY</a>
    <a style="left:884px">CONTACT</a>
    <a style="left:961px">SIGN UP!</a>
  </nav>
  <svg class="abs cart" width="12" height="11" viewBox="0 0 12 11" aria-label="Cart">
    <path d="M0 1h2l2 6h6l2-5H3" fill="none" stroke="#222" stroke-width="1.6"/>
    <rect x="3.5" y="2.5" width="7.5" height="4" fill="#222"/>
    <circle cx="4.5" cy="9.5" r="1.2" fill="#222"/><circle cx="9.5" cy="9.5" r="1.2" fill="#222"/>
  </svg>
</header>

<div class="abs steps">
  <span style="left:8px">1. YOUR STATUS</span>
  <span style="left:173px">2. PROPERTY TYPE</span>
  <span class="current" style="left:344px">3. QUOTE EXTRAS</span>
</div>

<h2 class="abs section-title" style="left:243px;top:274px">Searches</h2>
<div class="abs title-rule" style="left:243px;top:317px;width:161px"></div>
<div class="option" style="left:242px;top:361px;width:188px">BASIC<span class="info" style="left:149px">i</span></div>
<div class="option" style="left:434px;top:361px;width:188px">STANDARD<span class="info" style="left:149px">i</span></div>
<div class="option selected" style="left:626px;top:361px;width:188px">PREMIUM<span class="info" style="left:149px">i</span></div>
<div class="option" style="left:818px;top:361px;width:188px">NO SEARCHES<span class="info" style="left:149px">i</span></div>

<h2 class="abs section-title" style="left:240px;top:488px">Extensions</h2>
<div class="abs title-rule" style="left:242px;top:535px;width:186px"></div>
<div class="option selected" style="left:242px;top:566px;width:188px">UNLIMITED<span class="info" style="left:149px">i</span></div>
<div class="option" style="left:434px;top:566px;width:188px;padding-left:12px">NEEDED ONLY<span class="info" style="left:149px">i</span></div>

<h2 class="abs section-title" style="left:239px;top:694px">Contract risks</h2>
<div class="abs title-rule" style="left:242px;top:741px;width:237px"></div>
<div class="option" style="left:242px;top:766px;width:211px;padding-left:12px">TERMINATIONS<span class="info" style="left:172px">i</span></div>
<div class="option" style="left:457px;top:766px;width:252px">DEED OF RECESSIONS<span class="info" style="left:213px">i</span></div>
<div class="option selected" style="left:714px;top:766px;width:252px;border:none">DEED OF VARIATIONS<span class="info" style="left:214px">i</span></div>

<div class="abs tooltip" role="tooltip">
  <p>A <strong>Deed of Recession</strong> is a fancy legal word for a document that ‘rescinds’ or ‘takes back’ the agreement in an existing contract so that a new contract can be entered into.</p>
  <ul>
    <li>This normally happens when there are additional people that need to be added or any other changes to important parts of the con-tract.</li>
    <li>These are not normally expected, and when required can also mean unexpected fees.</li>
  </ul>
</div>

<span class="radio checked" style="top:883px"></span>
<span class="abs radio-label" style="top:884px">I have signed a contract</span>
<span class="radio" style="top:931px"></span>
<span class="abs radio-label" style="top:932px">I haven’t signed a contract</span>

<a class="btn btn-back">BACK</a>
<a class="btn btn-submit">SUBMIT</a>

</body>
</html>
```